Truck wrap - design for fleet

Take our current logo and design a wrap for our fleet of trucks.
Use our website as a guide: brightlane.ca. Trucks are white but can be wrapped fully orange.

Company colors are orange and black

Target Market(s)

Retail

Industry/Entity Type

Paving - driveways etc

Font styles to use
Sans Serif

Colors
F0912C
F2A743
F7CA91
FBE8D2
FDF5EE
EE7325
F08F49
F5BC92
FAE3D3
FDF4ED

Requirements
Must have
• Look awesome

```html
<!DOCTYPE html>
<html lang="en">
<head>
<meta charset="utf-8">
<title>Brightlane Paving – Fleet Wrap</title>
<link rel="stylesheet" href="https://fonts.googleapis.com/css2?family=Saira:ital,wght@0,700;0,800;1,800&display=swap">
<style>
  :root {
    --orange: #ee7325;
    --orange-deep: #e8661c;
    --white: #ffffff;
    --ink: #16232b;
    --backdrop: #d6d6d6;
  }
  * { margin: 0; padding: 0; box-sizing: border-box; }
  html, body { width: 1200px; height: 490px; overflow: hidden; background: var(--backdrop); }
  .wrap-canvas { position: relative; width: 1200px; height: 490px; font-family: "Saira", sans-serif; }
  .wrap-shapes { position: absolute; inset: 0; }
  .web-block {
    position: absolute; left: 150px; top: 148px; width: 300px;
    text-align: center; color: var(--white); font-weight: 800; font-size: 15px; line-height: 21px;
    letter-spacing: 0.3px;
  }
  .brand-name {
    position: absolute; left: 580px; top: 205px; width: 360px; text-align: center;
    color: var(--ink); font-weight: 800; line-height: 1;
  }
  .brand-name .word-main { display: block; font-size: 50px; letter-spacing: -0.5px; }
  .brand-name .word-sub { display: block; font-size: 32px; margin-top: 4px; letter-spacing: 0.5px; }
  .services {
    position: absolute; left: 610px; top: 316px; width: 300px; text-align: center;
    color: var(--ink); font-weight: 800; font-style: italic; font-size: 15.5px; letter-spacing: 0.2px;
    white-space: nowrap;
  }
</style>
</head>
<body>
<main class="wrap-canvas">
  <svg class="wrap-shapes" width="1200" height="490" viewBox="0 0 1200 490" aria-hidden="true">
    <!-- wrap panel -->
    <rect class="panel-orange" x="40" y="70" width="1120" height="350" rx="18" fill="var(--orange)"/>
    <!-- white front section -->
    <path class="panel-white-front" d="M920 70 H1142 A18 18 0 0 1 1160 88 V402 A18 18 0 0 1 1142 420 H930 L930 300 Z" fill="var(--white)"/>
    <!-- white band through middle -->
    <path class="band-white" d="M560 216 H895 L920 170 H960 L930 300 H570 Z" fill="var(--white)"/>
    <!-- band edge lines -->
    <path class="band-line" d="M560 220 H892 L914 178" stroke="var(--ink)" stroke-width="2" fill="none"/>
    <path class="band-line" d="M570 303 H935" stroke="var(--ink)" stroke-width="2" fill="none"/>
    <!-- accent rules beside sub-name -->
    <line x1="598" y1="286" x2="660" y2="286" stroke="var(--ink)" stroke-width="2"/>
    <line x1="860" y1="286" x2="922" y2="286" stroke="var(--ink)" stroke-width="2"/>
    <!-- emblem circle -->
    <circle class="emblem" cx="488" cy="243" r="100" fill="var(--white)"/>
    <circle class="emblem-ring" cx="488" cy="243" r="91" fill="none" stroke="var(--orange)" stroke-width="3"/>
  </svg>

  <div class="web-block">
    <p>BRIGHTLANE.CA</p>
    <p>PAVING THE WAY TO QUALITY</p>
  </div>

  <h1 class="brand-name">
    <span class="word-main">BRIGHTLANE</span>
    <span class="word-sub">PAVING</span>
  </h1>

  <p class="services">ASPHALT • INTERLOCK • SEALING</p>
</main>
</body>
</html>
```